I am looking for a Business Card Design for my spirit company titled "Harbor Pour Co" The company specializes in prohibition style/speakeasy mixology drinks and alcohol distribution. I am looking for Retro, Masculine, Sophisticated Card that embodies the look of Prohibition. Black and White colors. Also add Facebook, Instgram logo

Information that should go on the card is my Name, Title, Phone, Email, Website as follows:

Tobias K Verran
Principal
301.555.0187
tobias@harborpourco.example
harborpourco.example
Updates

Hello all I have uploaded a pdf version of the logo. It seems as if some are saying the resolution is too small.

Target Market(s)

Male and Female drinkers of all ages with a sophisticated palate that have an appreciation for fine crafted cocktail

Industry/Entity Type

Business

Requirements
Must have
• Information that should go on the card is my Name, Title, Phone, Email, Website as follows:

Tobias K Verran
Principal
301.555.0187
tobias@harborpourco.example
harborpourco.example

```html
<!DOCTYPE html>
<html lang="en">
<head>
<meta charset="utf-8">
<title>Harbor Pour Co — Business Card</title>
<link rel="stylesheet" href="https://fonts.googleapis.com/css2?family=Arimo:wght@400;700&family=Pinyon+Script&display=swap">
<style>
  :root {
    --backdrop: #d9d4cc;
    --card-edge: #ffffff;
    --card-ink: #2f2f2f;
    --card-glow: #4a4a4a;
    --type-light: #ffffff;
    --type-soft: #e6e6e6;
  }
  * { box-sizing: border-box; margin: 0; padding: 0; }
  html, body {
    width: 1200px; height: 801px; overflow: hidden;
    background: var(--backdrop);
    font-family: "Arimo", Arial, sans-serif;
  }
  .stage { position: relative; width: 1200px; height: 801px; }
  .card {
    position: absolute; top: 258px;
    width: 500px; height: 286px;
    border: 9px solid var(--card-edge);
    background: var(--card-ink);
    box-shadow: 0 6px 18px rgba(0,0,0,0.25);
    color: var(--type-light);
  }
  .card--front {
    left: 70px;
    background: radial-gradient(ellipse at 50% 45%, var(--card-glow) 0%, var(--card-ink) 70%);
  }
  .card--back { left: 630px; }

  /* Front: wordmark */
  .wordmark {
    position: absolute; left: 0; right: 0; top: 96px;
    display: flex; align-items: center; justify-content: center; gap: 14px;
  }
  .wordmark__dot {
    width: 22px; height: 22px; border-radius: 50%;
    background: var(--type-light);
  }
  .wordmark__name {
    font-weight: 700; font-size: 34px; letter-spacing: 0.5px;
  }
  .tagline {
    position: absolute; left: 0; right: 0; top: 152px;
    text-align: center; font-weight: 700; font-size: 10.5px;
    letter-spacing: 1.2px; text-transform: uppercase;
  }

  /* Back */
  .divider {
    position: absolute; left: 196px; top: 22px; bottom: 22px;
    width: 3px; background: var(--type-light);
  }
  .brand-small {
    position: absolute; right: 300px; top: 44px;
    font-weight: 700; font-size: 11px; white-space: nowrap;
  }
  .identity {
    position: absolute; right: 300px; top: 92px; text-align: right;
  }
  .identity__name { font-weight: 700; font-size: 17px; white-space: nowrap; }
  .identity__title {
    font-family: "Pinyon Script", cursive; font-size: 15px;
    color: var(--type-soft); margin-top: 2px;
  }
  .social {
    position: absolute; right: 300px; top: 160px;
    display: flex; gap: 4px;
  }
  .social__mark {
    width: 17px; height: 17px; border-radius: 3px;
    background: var(--type-light);
  }
  .contact {
    position: absolute; left: 206px; top: 38px;
    list-style: none; display: flex; flex-direction: column; gap: 16px;
  }
  .contact__item {
    display: flex; align-items: center; gap: 10px;
    font-size: 13.5px; white-space: nowrap;
  }
  .contact__icon { width: 28px; height: 28px; flex: none; }
</style>
</head>
<body>
<main class="stage">

  <section class="card card--front" aria-label="Card front">
    <div class="wordmark">
      <span class="wordmark__dot"></span>
      <span class="wordmark__name">Harbor Pour Co</span>
    </div>
    <p class="tagline">The Finest Speakeasy Pours</p>
  </section>

  <section class="card card--back" aria-label="Card back">
    <p class="brand-small">Harbor Pour Co</p>
    <div class="identity">
      <p class="identity__name">Tobias K Verran</p>
      <p class="identity__title">Principal</p>
    </div>
    <div class="social" role="img" aria-label="Social media links">
      <span class="social__mark"></span>
      <span class="social__mark"></span>
    </div>
    <span class="divider"></span>
    <ul class="contact">
      <li class="contact__item">
        <svg class="contact__icon" viewBox="0 0 28 28" aria-hidden="true">
          <circle cx="14" cy="14" r="13" fill="#fff"/>
          <rect x="9" y="6" width="10" height="16" rx="2" fill="none" stroke="#2f2f2f" stroke-width="2"/>
          <circle cx="14" cy="19" r="1" fill="#2f2f2f"/>
        </svg>
        <span>301.555.0187</span>
      </li>
      <li class="contact__item">
        <svg class="contact__icon" viewBox="0 0 28 28" aria-hidden="true">
          <circle cx="14" cy="14" r="13" fill="#fff"/>
          <rect x="6.5" y="9" width="15" height="10" rx="1" fill="none" stroke="#2f2f2f" stroke-width="2"/>
          <path d="M7 10 L14 15 L21 10" fill="none" stroke="#2f2f2f" stroke-width="2"/>
        </svg>
        <span>tobias@harborpourco.example</span>
      </li>
      <li class="contact__item">
        <svg class="contact__icon" viewBox="0 0 28 28" aria-hidden="true">
          <circle cx="14" cy="14" r="13" fill="#fff"/>
          <circle cx="14" cy="14" r="7.5" fill="none" stroke="#2f2f2f" stroke-width="1.8"/>
          <ellipse cx="14" cy="14" rx="3.2" ry="7.5" fill="none" stroke="#2f2f2f" stroke-width="1.5"/>
          <path d="M6.5 14 H21.5 M8 10 H20 M8 18 H20" stroke="#2f2f2f" stroke-width="1.3"/>
        </svg>
        <span>www.harborpourco.example</span>
      </li>
    </ul>
  </section>

</main>
</body>
</html>
```